Etiketten für neue Biermarke
Zielgruppe
Es soll eine neue Biermarke entwickelt werden. Die fünf grundlegenden Sorten sind: Pils, Radler, Helles, Hefeweizen, Alkoholfreies Hefeweizen. Für die neue Biermarke soll ein Markenname, ein Logo, ein Etikettendesign, ein Kistendesign und erste Werbeentwürfe gestaltet werden.
Das Bier soll durch Modernität, Massentauglichkeit und das gewisse Etwas überzeugen und sympathisch, qualitativ und „cool“ auf die Käufer wirken.
Die Zielgruppe der Biermarke sind eher junge Bierliebhaber. Das Bier soll im mittleren Preissegment verkauft werden.
Aufgabenstellung
Eurer Fantasie sind keine Grenzen gesetzt. Der Markenname kann beispielsweise ein Lebensgefühl oder eine Vision vermitteln, die unsere Biermarke widerspiegelt und positive Assoziationen bei den Käufern hervorruft. Das Design soll kreativ und modern sein und nicht klassisch wirken.
Unser Bier sollte weder in die Richtung Craft Bier noch in die Richtung klassisches Braubier gehen.

```html
<!DOCTYPE html>
<html lang="de">
<head>
<meta charset="UTF-8">
<title>Halbzeit – Radler Etikett</title>
<link rel="stylesheet" href="https://fonts.googleapis.com/css2?family=Montserrat:wght@400;800&display=swap">
<style>
  :root {
    --label-black: #0b0b0b;
    --ink-white: #f7f7f5;
    --band-yellow: #f7b70f;
    --band-ink: #1a1406;
    --page: #ffffff;
  }
  html, body {
    margin: 0;
    padding: 0;
    width: 1200px;
    height: 2373px;
    overflow: hidden;
    background: var(--page);
  }
  .canvas {
    position: relative;
    width: 1200px;
    height: 2373px;
  }
  .label {
    position: absolute;
    left: 186px;
    top: 1037px;
    width: 735px;
    height: 955px;
    background: var(--label-black);
    color: var(--ink-white);
    text-align: center;
  }
  .brand-dot {
    position: absolute;
    left: 50%;
    top: 150px;
    width: 56px;
    height: 56px;
    margin-left: -28px;
    border-radius: 50%;
    background: var(--ink-white);
  }
  .brand-name {
    position: absolute;
    left: 0;
    right: 0;
    top: 360px;
    margin: 0;
    font-family: "Montserrat", sans-serif;
    font-weight: 400;
    font-size: 104px;
    line-height: 1;
    letter-spacing: 8px;
    text-transform: uppercase;
    white-space: nowrap;
    color: var(--ink-white);
  }
  .tagline {
    position: absolute;
    left: 0;
    right: 0;
    top: 708px;
    margin: 0;
    font-family: "Montserrat", sans-serif;
    font-weight: 400;
    font-size: 24px;
    letter-spacing: 9px;
    text-transform: uppercase;
    white-space: nowrap;
  }
  .variety-band {
    position: absolute;
    left: 0;
    right: 0;
    top: 774px;
    height: 86px;
    background: var(--band-yellow);
    display: flex;
    align-items: center;
    justify-content: center;
  }
  .variety-name {
    margin: 0;
    font-family: "Montserrat", sans-serif;
    font-weight: 800;
    font-size: 54px;
    letter-spacing: 3px;
    color: var(--band-ink);
    text-transform: uppercase;
  }
</style>
</head>
<body>
  <main class="canvas">
    <section class="label" aria-label="Flaschenetikett Halbzeit Radler">
      <div class="brand-dot"></div>
      <h1 class="brand-name">Halbzeit</h1>
      <p class="tagline">Ein Bier für jeden Tag</p>
      <div class="variety-band">
        <h2 class="variety-name">Radler</h2>
      </div>
    </section>
  </main>
</body>
</html>
```